Create Lanternfield HR Business Cards.

Create Business Cards for Lanternfield HR. 2 sided and Would like the back to have the logo.

Info for Business Card:
Address: 4827 Millbrook Ave Suite 230 Cleveland, Ohio 44987
Office Number: 216-555-0143
Mobile: 216-555-0192

Website: www.lanternfieldhr.example

Target Market(s)

Small to medium size businesses

Industry/Entity Type

Human Resources

Contact Information for Business Card

Company logo and information

Font styles to use
Serif
Sans Serif

Requirements
Must have
• Info for Business Card: Address: 4827 Millbrook Ave Suite 230 Cleveland, Ohio 44987 Office Number: 216-555-0143 Mobile: 216-555-0192 Website: www.lanternfieldhr.example

```html
<!DOCTYPE html>
<html lang="en">
<head>
<meta charset="utf-8">
<title>Lanternfield HR Business Cards</title>
<link rel="stylesheet" href="https://fonts.googleapis.com/css2?family=Poppins:wght@400;500;600;700&display=swap">
<style>
  :root {
    --stage: #3f3b7c;
    --navy: #13112f;
    --navy-soft: #1d1a48;
    --orange: #f5861f;
    --white: #ffffff;
    --ink: #1c1a3a;
    --rule: #4b45b8;
  }
  * { box-sizing: border-box; margin: 0; padding: 0; }
  html, body { width: 1200px; height: 2400px; overflow: hidden; }
  body {
    background: var(--stage);
    font-family: "Poppins", sans-serif;
    position: relative;
  }
  .card {
    position: absolute;
    left: 147px;
    width: 905px;
    height: 517px;
    background: var(--navy);
    box-shadow: 0 10px 28px rgba(10, 8, 40, 0.35);
    overflow: hidden;
  }
  .card--front { top: 640px; }
  .card--back { top: 1230px; }

  .pattern-field {
    position: absolute;
    top: 0;
    background: radial-gradient(ellipse at 70% 35%, var(--navy-soft) 0%, rgba(29, 26, 72, 0.55) 55%, rgba(19, 17, 47, 0) 100%);
  }
  .card--front .pattern-field { left: 250px; width: 655px; height: 460px; }
  .card--back .pattern-field { left: 0; width: 452px; height: 380px; }

  .brand {
    position: absolute;
    display: flex;
    align-items: center;
    gap: 14px;
  }
  .brand__dot {
    width: 34px; height: 34px;
    border-radius: 50%;
    background: var(--orange);
    flex: none;
  }
  .brand__name {
    font-weight: 600;
    font-size: 38px;
    color: var(--white);
    letter-spacing: 0.5px;
    white-space: nowrap;
  }
  .card--front .brand { left: 65px; top: 250px; }
  .card--back .brand { left: 65px; top: 250px; }
  .card--back .brand__name { font-size: 32px; }

  .accent-line {
    position: absolute;
    height: 7px;
    background: var(--orange);
  }
  .card--front .accent-line { left: 65px; right: 0; top: 360px; }
  .card--back .accent-line { left: 65px; width: 387px; top: 364px; }

  .site {
    position: absolute;
    color: var(--white);
    font-weight: 400;
    white-space: nowrap;
  }
  .card--front .site { right: 70px; top: 398px; font-size: 28px; letter-spacing: 5.5px; }
  .card--back .site { left: 65px; top: 390px; font-size: 20px; letter-spacing: 3.4px; }

  .details {
    position: absolute;
    left: 452px; top: 0;
    width: 453px; height: 100%;
    background: var(--white);
    padding: 92px 40px 0 60px;
  }
  .person {
    display: flex;
    align-items: flex-end;
    gap: 10px;
  }
  .person__name {
    color: var(--orange);
    font-weight: 600;
    font-size: 32px;
    line-height: 0.98;
    text-transform: uppercase;
  }
  .person__role {
    color: var(--ink);
    font-size: 15px;
    letter-spacing: 3.5px;
    text-transform: uppercase;
    padding-bottom: 2px;
  }
  .details__rule {
    width: 298px;
    height: 2px;
    background: var(--rule);
    margin: 20px 0 28px;
  }
  .contact { list-style: none; }
  .contact__item {
    display: flex;
    align-items: flex-start;
    gap: 11px;
    font-size: 20px;
    line-height: 1.25;
    color: var(--ink);
    margin-bottom: 17px;
  }
  .contact__icon { width: 28px; height: 28px; flex: none; margin-top: 0; }
</style>
</head>
<body>

  <section class="card card--front" aria-label="Business card front">
    <div class="pattern-field" role="img" aria-label="Faint repeating brand pattern"></div>
    <div class="brand">
      <span class="brand__dot"></span>
      <span class="brand__name">Lanternfield HR</span>
    </div>
    <div class="accent-line"></div>
    <p class="site">www.lanternfieldhr.example</p>
  </section>

  <section class="card card--back" aria-label="Business card back">
    <div class="pattern-field" role="img" aria-label="Faint repeating brand pattern"></div>
    <div class="brand">
      <span class="brand__dot"></span>
      <span class="brand__name">Lanternfield HR</span>
    </div>
    <div class="accent-line"></div>
    <p class="site">www.lanternfieldhr.example</p>

    <div class="details">
      <div class="person">
        <h1 class="person__name">Dana<br>Whitcombe</h1>
        <span class="person__role">Founder</span>
      </div>
      <div class="details__rule"></div>
      <ul class="contact">
        <li class="contact__item">
          <svg class="contact__icon" viewBox="0 0 28 28" aria-hidden="true">
            <circle cx="14" cy="14" r="14" fill="#2b2870"/>
            <path d="M14 7a5 5 0 0 0-5 5c0 4 5 9 5 9s5-5 5-9a5 5 0 0 0-5-5z" fill="#fff"/>
            <circle cx="14" cy="12" r="2" fill="#2b2870"/>
          </svg>
          <span>4827 Millbrook Ave Suite 230<br>Cleveland, Ohio 44987</span>
        </li>
        <li class="contact__item">
          <svg class="contact__icon" viewBox="0 0 28 28" aria-hidden="true">
            <circle cx="14" cy="14" r="14" fill="#2b2870"/>
            <path d="M9.5 7.5l3 .2 1.2 3.2-1.8 1.3a9 9 0 0 0 4 4l1.3-1.8 3.2 1.2.2 3c-.3.9-1.3 1.4-2.4 1.2C12.6 19 9 15.4 8.3 10.3c-.2-1.1.3-2.5 1.2-2.8z" fill="#fff"/>
          </svg>
          <span>216-555-0143</span>
        </li>
        <li class="contact__item">
          <svg class="contact__icon" viewBox="0 0 28 28" aria-hidden="true">
            <circle cx="14" cy="14" r="14" fill="#2b2870"/>
            <rect x="10" y="7" width="8" height="14" rx="1.5" fill="#fff"/>
            <rect x="11.3" y="8.8" width="5.4" height="9" fill="#2b2870"/>
            <circle cx="14" cy="19.6" r="0.8" fill="#2b2870"/>
          </svg>
          <span>216-555-0192</span>
        </li>
        <li class="contact__item">
          <svg class="contact__icon" viewBox="0 0 28 28" aria-hidden="true">
            <circle cx="14" cy="14" r="14" fill="#2b2870"/>
            <g fill="none" stroke="#fff" stroke-width="1.4">
              <circle cx="14" cy="14" r="7"/>
              <ellipse cx="14" cy="14" rx="3" ry="7"/>
              <line x1="7" y1="14" x2="21" y2="14"/>
            </g>
          </svg>
          <span>www.lanternfieldhr.example</span>
        </li>
      </ul>
    </div>
  </section>

</body>
</html>
```